we are an outdoor outlet in a country club that has a variety of outlets. The Club is called Brindlewood and is located in Cairo, Egypt. This garden menu will include cuisines from the Mediterranean, Asia and Texmex. we need a menu that is colorful and would fit an A3 size, back and front are to be used. Attached is the old menu currently in use (Garden Menu 2012.pdf is just for reference) and the new menu text for you to use is under the name Garden Menu Fall 2013
thank you.

```html
<!DOCTYPE html>
<html lang="en">
<head>
<meta charset="utf-8">
<title>Brindlewood Country Club – Garden Menu</title>
<link href="https://fonts.googleapis.com/css2?family=Questrial&display=swap" rel="stylesheet">
<style>
  :root {
    --bg-top: #f7d9a6;
    --bg-mid: #f3c98c;
    --bg-low: #efb877;
    --panel: #f5edd2;
    --brown: #5b3a1f;
    --text: #5a2d17;
    --rule: #a08467;
    --oval: #c1b69c;
    --green: #9bb25a;
    --green-dark: #7e9a3e;
    --red-line: #c2322a;
    --white: #ffffff;
  }
  * { margin: 0; padding: 0; box-sizing: border-box; }
  html, body { width: 848px; height: 1200px; overflow: hidden; }
  body { font-family: "Questrial", "Century Gothic", sans-serif; color: var(--text); }

  .menu {
    position: relative; width: 848px; height: 1200px; overflow: hidden;
    background: linear-gradient(180deg, var(--bg-top) 0%, var(--bg-mid) 55%, var(--bg-low) 88%);
  }

  .ground-band {
    position: absolute; left: 0; right: 0; top: 1056px; bottom: 0;
    background: linear-gradient(180deg, var(--green) 0%, var(--green-dark) 100%);
    border-top: 5px solid var(--red-line);
  }

  .foliage { position: absolute; border-radius: 40%; }
  .foliage--top-left {
    left: 0; top: 0; width: 210px; height: 250px;
    background: radial-gradient(ellipse at 30% 30%, #e9892f 0%, #d8a53c 40%, rgba(247,217,166,0) 72%);
  }
  .foliage--top-right {
    right: 0; top: 0; width: 210px; height: 270px;
    background: radial-gradient(ellipse at 70% 30%, #e9892f 0%, #d8a53c 40%, rgba(247,217,166,0) 72%);
  }
  .foliage--bottom {
    left: 280px; top: 985px; width: 450px; height: 175px; z-index: 3;
    background: radial-gradient(ellipse at 45% 50%, #f3c21c 0%, #e7a431 30%, #c8732b 55%, rgba(200,115,43,0) 75%);
  }

  .brand {
    position: absolute; left: 0; right: 0; top: 66px; text-align: center; color: var(--brown);
  }
  .brand__name { font-size: 50px; line-height: 1; letter-spacing: 1px; }
  .brand__tagline { font-size: 20px; letter-spacing: 6px; margin-top: 4px; }

  .panel {
    position: absolute; background: var(--panel); border-radius: 24px; z-index: 2;
  }
  .panel--appetizers { left: 70px; top: 162px; width: 350px; height: 524px; }
  .panel--salads { left: 440px; top: 162px; width: 350px; height: 406px; }
  .panel--mediterranean { left: 70px; top: 698px; width: 350px; height: 332px; }
  .panel--desserts { left: 440px; top: 580px; width: 350px; height: 395px; }

  .panel__heading { position: absolute; left: 0; right: 0; height: 100px; }
  .panel__heading svg { position: absolute; left: 0; top: 0; }
  .panel__title {
    position: absolute; left: 0; right: 0; text-align: center; color: var(--brown);
    font-size: 37px; line-height: 1; top: 30px;
  }
  .panel__title--small { font-size: 20px; top: 38px; }

  .dish-list { position: absolute; left: 22px; right: 18px; list-style: none; }
  .dish-list--appetizers { top: 215px; font-size: 10.3px; line-height: 1.2; }
  .dish-list--appetizers li { margin-bottom: 9.5px; }
  .dish-list--desserts { top: 205px; font-size: 8.6px; line-height: 14.3px; }

  .salad { margin-bottom: 7px; }
  .salad__name { font-size: 15px; line-height: 1.1; }
  .salad__desc { font-size: 10.2px; line-height: 1.12; }
  .salad-list { position: absolute; left: 22px; right: 18px; top: 210px; }

  .soups { position: absolute; left: 22px; right: 14px; top: 172px; font-size: 10.2px; line-height: 1.2; }
  .soups__label { font-size: 14px; line-height: 1.1; }
  .soup { margin-bottom: 8px; }

  .site-url {
    position: absolute; left: 0; right: 0; top: 1162px; text-align: center;
    color: var(--white); font-size: 11px; letter-spacing: 0.5px; z-index: 4;
  }
</style>
</head>
<body>
<main class="menu">
  <div class="ground-band"></div>
  <div class="foliage foliage--top-left" role="img" aria-label="Autumn leaves, rowan berries, acorns and wheat in the corner"></div>
  <div class="foliage foliage--top-right" role="img" aria-label="Autumn leaves, rowan berries, acorns and wheat in the corner"></div>

  <header class="brand">
    <div class="brand__name">brindlewood</div>
    <div class="brand__tagline">country club</div>
  </header>

  <section class="panel panel--appetizers">
    <div class="panel__heading" style="top:88px">
      <svg width="350" height="100" viewBox="0 0 350 100">
        <ellipse cx="175" cy="8" rx="100" ry="12" fill="var(--oval)"/>
        <line x1="50" y1="29" x2="300" y2="29" stroke="var(--rule)" stroke-width="1"/>
        <circle cx="50" cy="29" r="2.5" fill="var(--rule)"/><circle cx="300" cy="29" r="2.5" fill="var(--rule)"/>
        <line x1="50" y1="90" x2="300" y2="90" stroke="var(--rule)" stroke-width="1"/>
        <circle cx="50" cy="90" r="2.5" fill="var(--rule)"/><circle cx="300" cy="90" r="2.5" fill="var(--rule)"/>
        <ellipse cx="175" cy="92" rx="100" ry="14" fill="var(--oval)" opacity="0.6"/>
      </svg>
      <h2 class="panel__title">appetizers</h2>
    </div>
    <ul class="dish-list dish-list--appetizers">
      <li>Salmon tartare seasoned with lemon juice, garlic,<br>&nbsp;&nbsp;and crushed black pepper</li>
      <li>Roasted eggplant rolls with herbed ricotta cheese and pine nuts</li>
      <li>Falafel in mini pita served with tehina and oriental salsa</li>
      <li>Mankousha with thyme and olive oil</li>
      <li>Fried kobeba with minced meat, spices, and pine nuts</li>
      <li>Fried calamari a la Romana served with aioli</li>
      <li>Samboussek with herbed white cheese and mint</li>
      <li>Oriental sausage sautéed with garlic and onion</li>
      <li>Mini vine leaves with a yoghurt dip</li>
      <li>Fatouch with a pomegranate syrup dressing</li>
      <li>Hummus seasoned with lemon juice, garlic, and olive oil</li>
      <li>White cheese with diced tomato, thyme, and olive oil</li>
      <li>Tehina seasoned with cumin, lemon juice, and garlic</li>
    </ul>
  </section>

  <section class="panel panel--salads">
    <div class="panel__heading" style="top:88px">
      <svg width="350" height="100" viewBox="0 0 350 100">
        <ellipse cx="175" cy="8" rx="100" ry="12" fill="var(--oval)"/>
        <line x1="50" y1="29" x2="300" y2="29" stroke="var(--rule)" stroke-width="1"/>
        <circle cx="50" cy="29" r="2.5" fill="var(--rule)"/><circle cx="300" cy="29" r="2.5" fill="var(--rule)"/>
        <line x1="50" y1="90" x2="300" y2="90" stroke="var(--rule)" stroke-width="1"/>
        <circle cx="50" cy="90" r="2.5" fill="var(--rule)"/><circle cx="300" cy="90" r="2.5" fill="var(--rule)"/>
        <ellipse cx="175" cy="92" rx="100" ry="14" fill="var(--oval)" opacity="0.6"/>
      </svg>
      <h2 class="panel__title">salads</h2>
    </div>
    <div class="salad-list">
      <div class="salad"><div class="salad__name">Caprese</div><div class="salad__desc">Buffalo mozzarella and sliced tomato with a balsamic vinaigrette</div></div>
      <div class="salad"><div class="salad__name">Rocket Apple</div><div class="salad__desc">Rocket leaves with gorgonzola, croutons, and<br>strawberry vinaigrette</div></div>
      <div class="salad"><div class="salad__name">French Riviera Nicoise</div><div class="salad__desc">Lettuce, egg, tomato, tuna, olives, onion, celery, radish,<br>bell pepper in a French vinaigrette</div></div>
      <div class="salad"><div class="salad__name">Folle</div><div class="salad__desc">Mixed greens with crab sticks, mushroom, corn, cherry tomato<br>in a mango vinaigrette</div></div>
    </div>
  </section>

  <section class="panel panel--mediterranean">
    <div class="panel__heading" style="top:94px">
      <svg width="350" height="100" viewBox="0 0 350 100">
        <ellipse cx="175" cy="8" rx="100" ry="12" fill="var(--oval)"/>
        <line x1="50" y1="20" x2="300" y2="20" stroke="var(--rule)" stroke-width="1"/>
        <circle cx="50" cy="20" r="2.5" fill="var(--rule)"/><circle cx="300" cy="20" r="2.5" fill="var(--rule)"/>
        <line x1="50" y1="64" x2="300" y2="64" stroke="var(--rule)" stroke-width="1"/>
        <circle cx="50" cy="64" r="2.5" fill="var(--rule)"/><circle cx="300" cy="64" r="2.5" fill="var(--rule)"/>
      </svg>
      <h2 class="panel__title panel__title--small" style="top:30px">mediterranean corner</h2>
    </div>
    <div class="soups">
      <div class="soups__label">Soups:</div>
      <div class="soup">Tomato Basil<br>Simmered tomato soup finished with fresh basil and cream</div>
      <div class="soup">Chicken Cream<br>Chicken broth with roasted chicken cubes, pine nuts, and cream</div>
      <div class="soup">Moroccan Harira<br>Vegetable broth with fresh tomato,<br>chickpeas, lentil, cilantro, and diced lamb</div>
    </div>
  </section>

  <section class="panel panel--desserts">
    <div class="panel__heading" style="top:86px">
      <svg width="350" height="100" viewBox="0 0 350 100">
        <ellipse cx="175" cy="8" rx="100" ry="12" fill="var(--oval)"/>
        <line x1="50" y1="29" x2="300" y2="29" stroke="var(--rule)" stroke-width="1"/>
        <circle cx="50" cy="29" r="2.5" fill="var(--rule)"/><circle cx="300" cy="29" r="2.5" fill="var(--rule)"/>
        <line x1="50" y1="90" x2="300" y2="90" stroke="var(--rule)" stroke-width="1"/>
        <circle cx="50" cy="90" r="2.5" fill="var(--rule)"/><circle cx="300" cy="90" r="2.5" fill="var(--rule)"/>
        <ellipse cx="175" cy="92" rx="100" ry="14" fill="var(--oval)" opacity="0.6"/>
      </svg>
      <h2 class="panel__title">desserts</h2>
    </div>
    <ul class="dish-list dish-list--desserts">
      <li>Mix Berries Cheesecake</li>
      <li>Crème Brulee</li>
      <li>Chocolate Caramel Cake</li>
      <li>Warm Chocolate Fondant</li>
      <li>Baked Apple Tart Tatin</li>
      <li>Tiramisu</li>
      <li>Pumpkin Pie Flan</li>
      <li>Mixed Berries Granola Yoghurt</li>
      <li>Vanilla Ice Cream Profiterole with dark and white chocolate sauce</li>
      <li>Caramelized Banana with Deep Fried Ice Cream</li>
      <li>Baklava with Nuts and Sugar Syrup</li>
      <li>Shot Glass Sampler – Tiramisu, Chocolate Crisp Mousse, Pear with Sabayon</li>
      <li>Ice Cream by Scoop</li>
    </ul>
  </section>

  <div class="foliage foliage--bottom" role="img" aria-label="Sunflower with autumn leaves, wheat ears and mushrooms"></div>

  <footer class="site-url">www.brindlewoodclub.net</footer>
</main>
</body>
</html>
```